Graphic Design of Business Process

We require an eye-catching, sophisticated design of 2 business processes (attached), that will be used digitally AND for print (to be put on walls in our office).

The basic layout is attached. We require a creative, professional designer to re-design these so that they look appealing but still able to grasp all the information.

We will require vector files and editable project files for final delivery. You may refer to our website (kitefieldmedia.com.au) for an indication of our brand.

If you have any questions, please ask.

Thank you.

```html
<!DOCTYPE html>
<html lang="en">
<head>
<meta charset="utf-8">
<title>Sales to Content Funnel &amp; Content Hierarchy</title>
<link rel="stylesheet" href="https://fonts.googleapis.com/css2?family=Roboto:wght@700;900&family=Lato:wght@400;700&display=swap">
<style>
  :root{
    --olive-dark:#6b5e00;
    --olive:#9c8700;
    --gold:#c4aa05;
    --gold-light:#cdb41a;
    --ink:#4a4a4a;
    --white:#ffffff;
    --orange:#f29a12;
    --panel-top:#f7f7f7;
    --panel-edge:#e2e2e2;
  }
  html,body{margin:0;padding:0;overflow:hidden;background:var(--white);}
  .sheet{width:800px;height:1200px;display:block;}
  .heading{font-family:"Roboto",Arial,sans-serif;font-weight:700;fill:var(--ink);font-size:36px;letter-spacing:0.2px;}
  .stage-title{font-family:"Lato",Arial,sans-serif;font-weight:700;fill:var(--white);font-size:17px;}
  .stage-sub{font-family:"Lato",Arial,sans-serif;font-weight:400;fill:var(--white);font-size:12px;}
  .stage-note{font-family:"Lato",Arial,sans-serif;font-weight:700;fill:var(--white);font-size:6.5px;}
  .tag-bold{font-family:"Lato",Arial,sans-serif;font-weight:700;fill:var(--white);font-size:10px;}
  .tag-text{font-family:"Lato",Arial,sans-serif;font-weight:400;fill:var(--white);font-size:10px;}
  .loop-label{font-family:"Lato",Arial,sans-serif;font-weight:700;fill:var(--ink);font-size:9.5px;}
  .tier-title{font-family:"Lato",Arial,sans-serif;font-weight:700;fill:var(--white);font-size:19px;}
  .tier-sub{font-family:"Lato",Arial,sans-serif;font-weight:400;fill:var(--white);font-size:17px;letter-spacing:0.3px;}
  .icon{fill:var(--white);}
  .icon-line{fill:none;stroke:var(--white);}
  .loop{fill:none;stroke:var(--orange);stroke-width:2.5;}
</style>
</head>
<body>
<svg class="sheet" viewBox="0 0 800 1200" xmlns="http://www.w3.org/2000/svg">
  <defs>
    <linearGradient id="panelFade" x1="0" y1="0" x2="1" y2="0">
      <stop offset="0" stop-color="#ffffff"/>
      <stop offset="0.5" stop-color="var(--panel-top)"/>
      <stop offset="1" stop-color="var(--panel-edge)"/>
    </linearGradient>
    <linearGradient id="panelFadeLow" x1="0" y1="0" x2="1" y2="0">
      <stop offset="0" stop-color="var(--panel-edge)"/>
      <stop offset="0.5" stop-color="#f4f4f4"/>
      <stop offset="1" stop-color="#ffffff"/>
    </linearGradient>
    <linearGradient id="goldSweep" x1="0" y1="0" x2="1" y2="0">
      <stop offset="0" stop-color="var(--olive-dark)"/>
      <stop offset="0.45" stop-color="var(--gold)"/>
      <stop offset="1" stop-color="var(--gold)"/>
    </linearGradient>
    <linearGradient id="goldShade" x1="0" y1="0" x2="1" y2="0">
      <stop offset="0" stop-color="var(--gold)"/>
      <stop offset="0.6" stop-color="var(--gold)"/>
      <stop offset="1" stop-color="var(--olive)"/>
    </linearGradient>
    <linearGradient id="tagSweep" x1="0" y1="0" x2="1" y2="0">
      <stop offset="0" stop-color="var(--olive-dark)"/>
      <stop offset="0.35" stop-color="var(--gold)"/>
      <stop offset="1" stop-color="var(--gold)"/>
    </linearGradient>
    <linearGradient id="hubShade" x1="0" y1="1" x2="1" y2="0">
      <stop offset="0" stop-color="var(--gold)"/>
      <stop offset="0.55" stop-color="var(--gold)"/>
      <stop offset="1" stop-color="var(--olive)"/>
    </linearGradient>
    <marker id="arrowHead" viewBox="0 0 10 10" refX="8" refY="5" markerWidth="6" markerHeight="6" orient="auto">
      <path d="M0 0 L10 5 L0 10 z" fill="var(--orange)"/>
    </marker>
  </defs>

  <rect class="panel panel--funnel" x="0" y="0" width="800" height="600" fill="url(#panelFade)"/>
  <rect class="panel panel--hierarchy" x="0" y="615" width="800" height="585" fill="url(#panelFadeLow)"/>

  <!-- Sales to content funnel -->
  <text class="heading" x="410" y="121" text-anchor="middle">SALES —&gt; CONTENT FUNNEL</text>

  <g class="funnel-tags">
    <rect x="590" y="180" width="160" height="48" fill="url(#tagSweep)"/>
    <text class="tag-bold" x="682" y="194" text-anchor="middle">PROBLEM &amp; SOLUTION</text>
    <text class="tag-text" x="682" y="207" text-anchor="middle">SUBJECT SHOWING</text>
    <text class="tag-text" x="682" y="220" text-anchor="middle">SYMPTOMS OF PROBLEM</text>

    <rect x="490" y="283" width="172" height="57" fill="url(#tagSweep)"/>
    <text class="tag-bold" x="596" y="296" text-anchor="middle">PROVIDERS &amp; TYPES</text>
    <text class="tag-bold" x="596" y="308" text-anchor="middle">OF SOLUTION</text>
    <text class="tag-text" x="596" y="320" text-anchor="middle">SUBJECT GIVES NAME</text>
    <text class="tag-text" x="596" y="332" text-anchor="middle">TO PROBLEM</text>

    <rect x="440" y="397" width="152" height="46" fill="url(#tagSweep)"/>
    <text class="tag-bold" x="528" y="422" text-anchor="middle">CONVERT &amp; RETAIN</text>
  </g>

  <g class="funnel-stages">
    <polygon class="stage stage--awareness" points="66,145 645,145 575,255 120,255" fill="url(#goldSweep)"/>
    <polygon class="stage stage--consideration" points="120,255 560,255 503,365 200,365" fill="url(#goldShade)"/>
    <polygon class="stage stage--decision" points="200,365 503,365 440,477 275,477" fill="url(#goldShade)"/>
    <polygon class="stage stage--tip" points="295,482 410,482 352,567" fill="var(--gold)"/>
  </g>

  <g class="stage-copy">
    <text class="stage-title" x="315" y="187" text-anchor="middle">AWARENESS</text>
    <text class="stage-sub" x="315" y="203" text-anchor="middle">IDENTIFY PROBLEM/NEED</text>
    <text class="stage-note" x="315" y="214" text-anchor="middle">- ASPIRATIONAL</text>
    <text class="stage-note" x="315" y="222" text-anchor="middle">- MARKET THE  OUTCOME NOT PRODUCT</text>

    <text class="stage-title" x="356" y="294" text-anchor="middle">CONSIDERATION</text>
    <text class="stage-sub" x="356" y="311" text-anchor="middle">EVALUATE ALTERNATIVES</text>
    <text class="stage-note" x="356" y="322" text-anchor="middle">- WHY IS THE SOLUTION BETTER THAN OTHERS</text>
    <text class="stage-note" x="356" y="330" text-anchor="middle">- HOW IS THIS PROVIDER GOING TO SOLVE MY NEED</text>

    <text class="stage-title" x="378" y="394" text-anchor="middle">ACTION/</text>
    <text class="stage-title" x="378" y="414" text-anchor="middle">DECISION</text>
    <text class="stage-sub" x="378" y="433" text-anchor="middle">PRESENT AN EFFER</text>
    <text class="stage-note" x="378" y="444" text-anchor="middle">- WHICH PROVIDER ?</text>
  </g>

  <g class="icon icon--bulb">
    <circle cx="190" cy="196" r="14"/>
    <rect x="183" y="208" width="14" height="14" rx="2"/>
    <rect x="182" y="224" width="16" height="3" rx="1.5"/>
    <rect x="184" y="229" width="12" height="3" rx="1.5"/>
    <path class="icon-line" d="M183 196 l5 5 l9 -9" stroke="var(--olive)" stroke-width="2.5"/>
    <g stroke="var(--white)" stroke-width="3" stroke-linecap="round">
      <line x1="190" y1="172" x2="190" y2="176"/>
      <line x1="173" y1="179" x2="176" y2="182"/>
      <line x1="207" y1="179" x2="204" y2="182"/>
      <line x1="165" y1="196" x2="169" y2="196"/>
      <line x1="211" y1="196" x2="215" y2="196"/>
      <line x1="168" y1="211" x2="172" y2="209"/>
      <line x1="212" y1="211" x2="208" y2="209"/>
    </g>
  </g>

  <g class="icon icon--chat">
    <path d="M212 298 h36 a4 4 0 0 1 4 4 v26 a4 4 0 0 1 -4 4 h-6 v6 l-8 -6 h-22 a4 4 0 0 1 -4 -4 v-26 a4 4 0 0 1 4 -4z" fill="var(--white)" stroke="var(--gold)" stroke-width="2"/>
    <path d="M194 286 h36 a4 4 0 0 1 4 4 v26 a4 4 0 0 1 -4 4 h-22 l-10 8 v-8 h-4 a4 4 0 0 1 -4 -4 v-26 a4 4 0 0 1 4 -4z" fill="var(--white)" stroke="var(--gold)" stroke-width="2"/>
    <circle cx="204" cy="303" r="2.6" fill="var(--gold)"/>
    <circle cx="212" cy="303" r="2.6" fill="var(--gold)"/>
    <circle cx="220" cy="303" r="2.6" fill="var(--gold)"/>
  </g>

  <g class="icon icon--gears">
    <circle cx="278" cy="420" r="13"/>
    <circle cx="278" cy="420" r="16" fill="none" stroke="var(--white)" stroke-width="7" stroke-dasharray="6 6.5"/>
    <circle cx="278" cy="420" r="5" fill="var(--gold)"/>
    <circle cx="300" cy="400" r="7"/>
    <circle cx="300" cy="400" r="9" fill="none" stroke="var(--white)" stroke-width="4" stroke-dasharray="3.5 3.6"/>
    <circle cx="300" cy="400" r="3" fill="var(--gold)"/>
  </g>

  <g class="feedback-loops">
    <path class="loop" d="M610 459 C 700 455, 755 400, 752 330 C 750 270, 700 240, 605 238" marker-end="url(#arrowHead)"/>
    <path class="loop" d="M610 459 C 690 455, 735 410, 720 380 C 705 355, 650 352, 518 352" marker-end="url(#arrowHead)"/>
    <path class="loop" d="M610 459 L 446 459" marker-end="url(#arrowHead)"/>
    <text class="loop-label" x="572" y="456" text-anchor="middle">WOM &amp;</text>
    <text class="loop-label" x="572" y="469" text-anchor="middle">REFERRAL</text>
  </g>

  <!-- Content hierarchy -->
  <text class="heading" x="423" y="706" text-anchor="middle">CONTENT HIERARCHY</text>

  <g class="tier tier--hero">
    <rect x="182" y="733" width="471" height="127" fill="url(#goldSweep)"/>
    <rect x="205" y="752" width="80" height="85" rx="10" fill="var(--gold-light)" opacity="0.55" role="img" aria-label="Flexed arm with cape icon"/>
    <text class="tier-title" x="414" y="788" text-anchor="middle">HERO</text>
    <text class="tier-sub" x="414" y="816" text-anchor="middle">TENTPOLE CAMPAIGNS</text>
  </g>

  <g class="tier tier--hub">
    <rect x="165" y="862" width="472" height="126" fill="url(#hubShade)"/>
    <g class="icon icon--network">
      <g stroke="var(--white)" stroke-width="3">
        <line x1="238" y1="932" x2="215" y2="897"/>
        <line x1="238" y1="932" x2="257" y2="914"/>
        <line x1="238" y1="932" x2="209" y2="941"/>
        <line x1="238" y1="932" x2="253" y2="955"/>
      </g>
      <circle cx="238" cy="932" r="12" fill="var(--gold)" stroke="var(--white)" stroke-width="3"/>
      <circle cx="213" cy="894" r="7" fill="var(--gold)" stroke="var(--white)" stroke-width="3"/>
      <circle cx="259" cy="913" r="7" fill="var(--gold)" stroke="var(--white)" stroke-width="3"/>
      <circle cx="207" cy="942" r="7" fill="var(--gold)" stroke="var(--white)" stroke-width="3"/>
      <circle cx="255" cy="957" r="7" fill="var(--gold)" stroke="var(--white)" stroke-width="3"/>
    </g>
    <text class="tier-title" x="414" y="908" text-anchor="middle">HUB</text>
    <text class="tier-sub" x="414" y="937" text-anchor="middle">REGULAR ``PUSH” CONTENT</text>
  </g>

  <g class="tier tier--hygiene">
    <rect x="182" y="990" width="471" height="127" fill="var(--gold)"/>
    <g class="icon icon--shower">
      <path d="M206 1037 a16 16 0 0 1 32 0 z"/>
      <path class="icon-line" d="M222 1021 v-5 a10 10 0 0 1 20 0 v71" stroke-width="5"/>
      <g>
        <ellipse cx="209" cy="1047" rx="2.2" ry="3"/>
        <ellipse cx="218" cy="1047" rx="2.2" ry="3"/>
        <ellipse cx="227" cy="1047" rx="2.2" ry="3"/>
        <ellipse cx="236" cy="1047" rx="2.2" ry="3"/>
        <ellipse cx="209" cy="1057" rx="2.2" ry="3"/>
        <ellipse cx="218" cy="1057" rx="2.2" ry="3"/>
        <ellipse cx="227" cy="1057" rx="2.2" ry="3"/>
        <ellipse cx="236" cy="1057" rx="2.2" ry="3"/>
        <ellipse cx="209" cy="1067" rx="2.2" ry="3"/>
        <ellipse cx="218" cy="1067" rx="2.2" ry="3"/>
        <ellipse cx="227" cy="1067" rx="2.2" ry="3"/>
        <ellipse cx="236" cy="1067" rx="2.2" ry="3"/>
      </g>
    </g>
    <text class="tier-title" x="414" y="1040" text-anchor="middle">HYGIENE</text>
    <text class="tier-sub" x="414" y="1070" text-anchor="middle">ALWAYS-ON ``PULL” CONTENT</text>
  </g>
</svg>
</body>
</html>
```